Business card design needed

see my website

www.aldermoorandpike.com

I am after a new logo and business card needs to fit in with the website. I like the look of typewriter text - would like this on the website as well if I could!

Industry/Entity Type

Business

Contact Information for Business Card

Aldermoor and Pike
Design and Heritage Consultants

Marisa Oakton
Principal

+61 407 963 215
marisa@aldermoorandpike.com

www.aldermoorandpike.com

back of card

Interior Design
Consultancy on Period Home restoration and renovation
Heritage Impact Statements
Conservation Management Plans
Materials Conservation
Historical Research

```html
<!DOCTYPE html>
<html lang="en">
<head>
<meta charset="utf-8">
<title>Aldermoor &amp; Pike – Design and Heritage Consultants</title>
<link rel="stylesheet" href="https://fonts.googleapis.com/css2?family=Special+Elite&display=swap">
<style>
  :root {
    --ink-bg: #272727;
    --paper-white: #f4f4f2;
    --accent-orange: #f0861f;
  }
  html, body {
    margin: 0;
    padding: 0;
    overflow: hidden;
    background: var(--ink-bg);
  }
  .card {
    position: relative;
    width: 1200px;
    height: 693px;
    background: var(--ink-bg);
    color: var(--paper-white);
    font-family: "Special Elite", "Courier New", monospace;
    overflow: hidden;
  }
  .card__frame {
    position: absolute;
    inset: 0;
  }
  .brand-mark {
    position: absolute;
    left: 553px;
    top: 66px;
    width: 94px;
    height: 94px;
    border-radius: 50%;
    background: var(--accent-orange);
  }
  .brand-name {
    position: absolute;
    left: 0;
    right: 0;
    top: 194px;
    margin: 0;
    text-align: center;
    font-size: 56px;
    font-weight: 400;
    letter-spacing: 1px;
    line-height: 1;
  }
  .brand-tagline {
    position: absolute;
    left: 0;
    right: 0;
    top: 268px;
    margin: 0;
    text-align: center;
    font-size: 30px;
    line-height: 1;
  }
  .services {
    position: absolute;
    left: 194px;
    top: 358px;
    margin: 0;
    padding: 0;
    list-style: none;
    font-size: 31px;
    line-height: 50.8px;
  }
</style>
</head>
<body>
  <main class="card">
    <svg class="card__frame" width="1200" height="693" viewBox="0 0 1200 693" aria-hidden="true">
      <g stroke="var(--paper-white)" fill="none">
        <line class="rule rule--top" x1="226" y1="339" x2="977" y2="339" stroke-width="3" stroke-dasharray="14 9"/>
        <line class="rule rule--bottom" x1="226" y1="621" x2="977" y2="621" stroke-width="3" stroke-dasharray="14 9"/>
        <path class="brace brace--left" stroke-width="9" stroke-linecap="round"
              d="M165 343 C135 343 124 356 124 385 L124 450 C124 472 108 482 70 483
                 C108 484 124 494 124 516 L124 582 C124 610 135 623 165 623"/>
        <path class="brace brace--right" stroke-width="9" stroke-linecap="round"
              d="M1035 343 C1065 343 1076 356 1076 385 L1076 450 C1076 472 1092 482 1130 483
                 C1092 484 1076 494 1076 516 L1076 582 C1076 610 1065 623 1035 623"/>
      </g>
    </svg>

    <div class="brand-mark" aria-hidden="true"></div>
    <h1 class="brand-name">ALDERMOOR &amp; PIKE</h1>
    <p class="brand-tagline">design and heritage consultants</p>

    <ul class="services">
      <li>Interior Design Consultancy on Period Homes</li>
      <li>restoration and renovation</li>
      <li>Heritage Impact Statements</li>
      <li>Conservation Management Plans Materials</li>
      <li>Conservation Historical Research</li>
    </ul>
  </main>
</body>
</html>
```